Terravane Business Card Design

We need a modern, clean, business card design for our hardscape solution company. I have outlined our specialist areas in the card information section. We meet and greet and wish to build relationships with large-scale builders and project managers of large-scale building companies. Hence the reason for the business card.We want them to understand we are their 'solution' and we will make their working life easier and less stressful. We also are the highest quality construction with an exceptional eye for detail taking a lot of pressure off the project managers. I have done a few mock-ups myself but would like to see what else can be created. We are open to black or white (or grey) background.

Industry/Entity Type

Construction

Contact Information for Business Card

Mark Quinlow - Director
0417 583 902
mark@terravanegroup.com

www.terravanegroup.com.au

"Hardscape Construction Solutions for Large-Scale Builders" (front)

Logo already designed and to be added.

REAR:

Your One-Stop Hardscape Solution For:

Retirement Village & Community Development Construction

- Synthetic Sports Fields - Bowling Greens
- Tennis Courts - Concreting
- Paving - Landscape

www.terravanegroup.com

```html
<!DOCTYPE html>
<html lang="en">
<head>
<meta charset="utf-8">
<title>Terravane Business Card</title>
<link href="https://fonts.googleapis.com/css2?family=Didact+Gothic&display=swap" rel="stylesheet">
<style>
  :root{
    --page:#e9e7e2;
    --olive-deep:#2f360c;
    --olive:#4f5a17;
    --lime:#a9c62e;
    --lime-light:#c9dc7a;
    --lime-dark:#8fae1f;
    --blue:#1a8ed3;
    --grey:#6b6b6b;
    --ink:#3a3a3a;
    --white:#ffffff;
  }
  *{margin:0;padding:0;box-sizing:border-box}
  html,body{width:1200px;height:784px;overflow:hidden}
  body{background:var(--page);font-family:"Didact Gothic",sans-serif;position:relative}
  .card{position:absolute;top:227px;width:540px;height:330px;overflow:hidden;box-shadow:0 6px 18px rgba(0,0,0,.18)}
  .card--rear{left:40px;color:var(--white)}
  .card--front{left:620px;background:var(--white)}

  /* rear */
  .rear-field{position:absolute;inset:0;background:
      radial-gradient(ellipse at 85% 25%, var(--lime) 0%, var(--lime-dark) 22%, transparent 60%),
      linear-gradient(110deg, var(--olive-deep) 0%, var(--olive) 55%, var(--lime-dark) 100%)}
  .rear-heading{position:absolute;top:26px;left:0;right:0;text-align:center;font-size:15px}
  .rear-sector{position:absolute;top:56px;left:30px;right:20px;text-align:center;font-size:13px}
  .rear-services{position:absolute;top:104px;left:50px;list-style:none;font-size:19px;line-height:27px}
  .rear-services li::before{content:"•";margin-right:8px}
  .rear-brand{position:absolute;right:40px;top:200px;font-size:32px;color:var(--white)}

  /* front */
  .front-swoosh{position:absolute;inset:0}
  .front-brand{position:absolute;left:48px;top:70px;font-size:56px;color:var(--blue);letter-spacing:-1px}
  .front-name{position:absolute;left:50px;top:166px;font-size:20px;color:var(--blue)}
  .front-role{position:absolute;left:50px;top:192px;font-size:13px;color:var(--grey)}
  .front-contacts{position:absolute;left:50px;top:216px;list-style:none;font-size:15px;line-height:22px;color:var(--ink)}
  .front-contacts li{display:flex;align-items:center;gap:7px}
  .front-contacts svg{width:14px;height:14px;flex:none}
  .front-tagline{position:absolute;right:22px;bottom:9px;font-size:10px;letter-spacing:2.6px;text-transform:uppercase;color:var(--white)}
</style>
</head>
<body>
  <section class="card card--rear">
    <div class="rear-field" role="img" aria-label="Decorative pattern of overlapping lime ovals on dark olive"></div>
    <p class="rear-heading">Your One-Stop Hardscape Solution For:</p>
    <p class="rear-sector">Retirement Village &amp; Community Development Construction</p>
    <ul class="rear-services">
      <li>Synthetic Sports Fields</li>
      <li>Bowling Greens</li>
      <li>Tennis Courts</li>
      <li>Concreting</li>
      <li>Paving</li>
      <li>Landscape</li>
    </ul>
    <p class="rear-brand">Terravane</p>
  </section>

  <section class="card card--front">
    <svg class="front-swoosh" viewBox="0 0 540 330" preserveAspectRatio="none" aria-hidden="true">
      <path d="M0 300 C210 306 390 268 540 170 L540 330 L0 330 Z" fill="var(--lime-light)"/>
      <path d="M0 306 C210 310 392 274 540 180 L540 330 L0 330 Z" fill="var(--lime)"/>
    </svg>
    <p class="front-brand">Terravane</p>
    <p class="front-name">Mark Quinlow</p>
    <p class="front-role">Director</p>
    <ul class="front-contacts">
      <li><svg viewBox="0 0 16 16"><path d="M3 1l3 3-1.5 2a9 9 0 0 0 5.5 5.5L12 10l3 3-2 2C7 15 1 9 1 3z" fill="var(--blue)"/></svg>0417 583 902</li>
      <li><svg viewBox="0 0 16 16"><rect x="1" y="3" width="14" height="10" rx="1.5" fill="var(--blue)"/><path d="M1.5 4l6.5 5 6.5-5" fill="none" stroke="var(--white)" stroke-width="1.3"/></svg>mark@terravanegroup.com</li>
      <li><svg viewBox="0 0 16 16"><circle cx="8" cy="8" r="6.5" fill="none" stroke="var(--blue)" stroke-width="1.4"/><ellipse cx="8" cy="8" rx="3" ry="6.5" fill="none" stroke="var(--blue)" stroke-width="1.2"/><path d="M1.5 8h13" stroke="var(--blue)" stroke-width="1.2"/></svg>www.terravanegroup.com.au</li>
    </ul>
    <p class="front-tagline">Hardscape Construction Solutions for Large-Scale Builders</p>
  </section>
</body>
</html>
```